Industrial Company needing new business cards

We are a newly branded Industrial trade company. We specialise in Electrical, Mechanical and Air-conditioning.

I would like to see designs single sided. Focusing on the color scheme white/red/black and possibly gray. Possibly make it a black card with white writting... but open to all designs.

I would like the design to be professional, sleek and to the point.

Industry/Entity Type

Business

Contact Information for Business Card

Tom Harwick
Managing Director / Electrician
tomwork@velnet.com.au
47 Garnet Road, Rutherford NSW 2320
Mobile: 0427115830
www.harwickindustrialgroup.com.au

Requirements
Must have
• Must be able to be sent in a manner that i can change the details for each employee.
• Our logo
Nice to have
• Would like it to somehow have " incorporating Talvo Group Pty Ltd" as this is the company we have taken over.
Should not have
• No yellow!!!
• must not simply place "talvo group" randomly on the business card. refer nice to have.

```html
<!DOCTYPE html>
<html lang="en">
<head>
<meta charset="utf-8">
<title>Harwick Industrial Group – Business Card</title>
<link rel="stylesheet" href="https://fonts.googleapis.com/css2?family=Titillium+Web:wght@300;400;600;700&display=swap">
<style>
  :root {
    --stage: #34434b;
    --card-black: #050505;
    --brand-red: #e41c24;
    --white: #ffffff;
    --grey: #a7a9ac;
    --grey-dark: #8c8e91;
    --card-w: 900px;
    --card-h: 550px;
  }
  * { box-sizing: border-box; margin: 0; padding: 0; }
  html, body {
    width: 1200px; height: 1200px; overflow: hidden;
    background: var(--stage);
    font-family: "Titillium Web", sans-serif;
  }
  .stage {
    width: 1200px; height: 1200px;
    display: flex; flex-direction: column; align-items: center; justify-content: center;
    gap: 40px;
  }
  .card {
    position: relative;
    width: var(--card-w); height: var(--card-h);
    background: var(--card-black);
    overflow: hidden;
    box-shadow: 0 14px 30px rgba(0,0,0,.35);
  }

  /* Brand name lockup */
  .brand { display: flex; align-items: flex-start; gap: 22px; }
  .brand-square { background: var(--brand-red); flex: none; }
  .brand-name {
    color: var(--white); font-weight: 700; text-transform: uppercase;
    line-height: .95; letter-spacing: .04em;
  }
  .brand-tagline {
    color: var(--grey); font-weight: 600; text-transform: uppercase; letter-spacing: .08em;
    white-space: nowrap;
  }

  /* Front */
  .card-front .brand-block { position: absolute; left: 110px; top: 140px; }
  .card-front .brand-square { width: 120px; height: 120px; margin-top: 6px; }
  .card-front .brand-name { font-size: 54px; }
  .card-front .brand-tagline { font-size: 22px; margin-top: 22px; }

  /* Back */
  .red-panel { position: absolute; inset: 0; width: 100%; height: 100%; }
  .website {
    position: absolute; left: 40px; bottom: 40px;
    display: flex; align-items: center; gap: 8px;
    color: var(--white); font-size: 22px; white-space: nowrap;
  }
  .website strong { font-weight: 700; font-style: italic; }
  .website span { font-weight: 300; }
  .person { position: absolute; right: 60px; top: 34px; text-align: right; }
  .person-name { color: var(--white); font-size: 38px; font-weight: 700; letter-spacing: .02em; }
  .person-title { color: var(--grey); font-size: 24px; font-weight: 400; margin-top: -4px; }
  .divider { width: 230px; height: 2px; background: var(--white); margin: 24px 0 20px auto; }
  .contact { display: flex; justify-content: flex-end; align-items: center; gap: 18px;
    color: var(--white); font-size: 32px; font-weight: 400; letter-spacing: .03em; line-height: 1.4; }
  .contact svg { width: 30px; height: 30px; flex: none; }
  .card-back .brand-block { position: absolute; right: 60px; top: 335px; }
  .card-back .brand-square { width: 62px; height: 62px; margin-top: 4px; }
  .card-back .brand { gap: 14px; }
  .card-back .brand-name { font-size: 30px; }
  .card-back .brand-tagline { font-size: 13px; margin-top: 8px; color: var(--white); }
  .incorporating {
    position: absolute; right: 60px; bottom: 40px;
    color: var(--grey-dark); font-size: 20px; font-weight: 400; text-transform: uppercase;
    white-space: nowrap;
  }
</style>
</head>
<body>
<main class="stage">

  <section class="card card-front" aria-label="Card front">
    <div class="brand-block">
      <div class="brand">
        <div class="brand-square"></div>
        <div class="brand-name">Harwick<br>Industrial<br>Group</div>
      </div>
      <div class="brand-tagline">Electrical - Mechanical - Airconditioning</div>
    </div>
  </section>

  <section class="card card-back" aria-label="Card back">
    <svg class="red-panel" viewBox="0 0 900 550" aria-hidden="true">
      <polygon points="0,0 40,0 465,550 0,550" fill="var(--brand-red)"/>
      <line x1="40" y1="0" x2="465" y2="550" stroke="var(--white)" stroke-width="8"/>
    </svg>

    <div class="website">
      <svg width="26" height="26" viewBox="0 0 24 24" fill="none" stroke="#fff" stroke-width="2.4" stroke-linecap="round" stroke-linejoin="round" aria-hidden="true">
        <path d="M10 5H5v14h14v-5"/><path d="M13 3h8v8"/><path d="M21 3 11 13"/>
      </svg>
      <div><strong>harwickindustrialgroup</strong><span>.com.au</span></div>
    </div>

    <div class="person">
      <div class="person-name">Tom Harwick</div>
      <div class="person-title">Managing Director / Electrician</div>
      <div class="divider"></div>
      <div class="contact">0427115830
        <svg viewBox="0 0 24 24" fill="#fff" aria-hidden="true"><path d="M6.6 10.8a15.1 15.1 0 0 0 6.6 6.6l2.2-2.2a1 1 0 0 1 1-.25 11.4 11.4 0 0 0 3.6.57 1 1 0 0 1 1 1V20a1 1 0 0 1-1 1A17 17 0 0 1 3 4a1 1 0 0 1 1-1h3.5a1 1 0 0 1 1 1c0 1.25.2 2.45.57 3.57a1 1 0 0 1-.25 1z"/></svg>
      </div>
      <div class="contact">tomwork@velnet.com.au
        <svg viewBox="0 0 24 24" fill="#fff" aria-hidden="true"><path d="M2 5h20v14H2z"/><path d="M2 5l10 8 10-8" fill="none" stroke="#050505" stroke-width="1.8"/></svg>
      </div>
    </div>

    <div class="brand-block">
      <div class="brand">
        <div class="brand-square"></div>
        <div class="brand-name">Harwick<br>Industrial<br>Group</div>
      </div>
      <div class="brand-tagline">Electrical - Mechanical - Airconditioning</div>
    </div>

    <div class="incorporating">Incorporating Talvo Group Pty Ltd</div>
  </section>

</main>
</body>
</html>
```